a Label for a candle jar and its gift box

I would like a label that is modern minimalist for candles jars. These jars are colored as white, amber and black. I am thinking maybe foiling gold/silver background with logo only and maybe company name in different color that suits the foiling background color/s. I would like a high quality luxurious design that shows the preciousness of this candle. I am open to any ideas you might have for the design but so far I have used a logo only on the jar which I really like BUT I still feel that it is not enough branding for people when you only show them the logo so I am considering adding the business name. Again, I am open to both ideas (with logo only or logo with business name (Silken Meadow).

IMPORTANT: YOU MAY IGNORE MY DESIGN COMPLETELY AND DO YOUR OWN ONE AS LONG AS YOU KERP THE LOGO DESIGN. YOU MAY ALSO ADJUST THE LOGO A BIT TO SUIT YOUR DESIGN. - sorry im using capital letters to show importance but im not yelling :)

UPDATE: To clarify, I have uploaded a video called Corvel in the box to show what the current product look like. It is a corvel jar with a logo only and the jar box has a window that shows the jar with the logo on it and the back of that jar box has a bigger version of the label that has more details (i.e. Fragrance name and website link). So to make it clear, I would like to have two versions of the lables: 1. on the jar with minimal info (logo only or logo with the business name) 2. Bigger version of the label with more info to put on the back of the jar box - as described above. The dimensions of the jars are as per this link https://www.lunaxo-example.com.au/corvel-medium-base-and-flat-lid-amber-packed-with-lid-on/ The dimensions of the jar box as per this link https://www.lunaxo-example.com.au/corvel-medium-flat-lid-candle-box-with-window-beige/ Looking forward to some artistic productions :)

Update #2: Tues 25 Dec 18 1. I have uploaded the photo which has the logo with the name 'Silken Meadow' below it just for a reference. However, I would like the designer to modify the current font and NOT to use it as the word 'of in the phrase 'Silken Meadow' does not come out clear enough after printing. 2. I would like the designer NOT to create a design that will require a clear sticker/label for printing. 3. I have attached the photos of my current designs on the jars or the jar box just as a reference but please do NOT just use the same fonts and only change background. I am hoping to see something different and more professional than my own design :) Thank you very much!

Font styles to use
Decorative
Script

Requirements
Must have
• I would like them to fit on the three colors of the jars below - white, amber and black. Below is a link to how the jar looks like https://www.lunaxo-example.com.au/candle-making-supplies/candle-jars/corvel-candle-jars/?glassware_colour=415,443,417&glassware_size=268
Nice to have
• I would like to have a modern design which is suitable for both feminine and musculine.
Should not have
• shouldnt have so much writing on it!

```html
<!DOCTYPE html>
<html lang="en">
<head>
<meta charset="utf-8">
<title>Silken Meadow – Turkish Rose jar label and gift box</title>
<link href="https://fonts.googleapis.com/css2?family=Marcellus&family=Montserrat:wght@400;500&display=swap" rel="stylesheet">
<style>
  :root{
    --stage:#d9c4b5;
    --paper:#ffffff;
    --pattern:#f3f3f3;
    --dieline:#d6d6d6;
    --ink:#1b1b1b;
    --rose:#ef7472;
    --gold:#f2c12c;
    --white:#ffffff;
  }
  *{margin:0;padding:0;box-sizing:border-box}
  html,body{width:1200px;height:1200px;overflow:hidden;background:var(--paper)}
  .canvas{position:relative;width:1200px;height:1200px;font-family:"Marcellus",serif;color:var(--ink)}
  .stage{position:absolute;left:0;top:0;width:1200px;height:676px;background:var(--stage)}

  /* jar label, flat */
  .jar-label{position:absolute;left:440px;top:168px;width:320px;height:340px;border-radius:22px;background:var(--gold);
    display:flex;flex-direction:column;align-items:center;color:var(--white)}
  .jar-label__name{margin-top:24px;font-size:27px;letter-spacing:.5px;font-family:"Marcellus",serif}
  .jar-label__mark{margin-top:48px;width:110px;height:110px;border-radius:50%;border:3px solid var(--white)}
  .jar-label__scent{position:absolute;bottom:26px;left:0;right:0;display:flex;align-items:center;gap:14px;padding:0 0;
    font-family:"Montserrat",sans-serif;font-size:12px;letter-spacing:4px}
  .jar-label__scent::before,.jar-label__scent::after{content:"";flex:1;height:1px;background:var(--white)}

  /* dieline */
  .dieline{position:absolute;left:162px;top:698px;width:876px;height:470px}
  .panel{position:absolute;border:1px solid var(--dieline);background:var(--paper)}
  .pattern{position:absolute;background:var(--pattern)}
  .lid{left:0;top:0;width:222px;height:178px;border-radius:32px 32px 0 0;overflow:hidden}
  .lid .pattern{inset:0}
  .lid__plate{position:absolute;left:36px;top:64px;width:150px;height:80px;background:var(--paper);
    display:flex;align-items:center;justify-content:center;transform:rotate(180deg);font-size:15px}
  .face{top:178px;height:292px}
  .face--front{left:0;width:222px}
  .face--side-a{left:222px;width:216px}
  .face--window{left:438px;width:222px}
  .face--side-b{left:660px;width:216px}

  .lockup{position:absolute;left:0;right:0;display:flex;flex-direction:column;align-items:center}
  .lockup__dot{width:14px;height:14px;border-radius:50%;border:1.5px solid var(--ink);margin-bottom:8px}
  .lockup__name{line-height:.95;text-align:center}
  .scent-band{display:inline-block;background:var(--rose);color:var(--white);border-radius:4px;margin-top:8px}

  .face--front .lockup{top:62px}
  .face--front .lockup__name{font-size:29px}
  .face--front .scent-band{font-size:15px;padding:2px 12px}
  .face--side-a .lockup,.face--side-b .lockup{top:94px}
  .face--side-a .lockup__name,.face--side-b .lockup__name{font-size:23px}
  .face--side-a .scent-band,.face--side-b .scent-band{font-size:11px;padding:2px 9px}

  .contact{position:absolute;left:0;right:0;bottom:18px;text-align:center;font-family:"Montserrat",sans-serif;font-size:6.5px;line-height:1.6}
  .contact__web{letter-spacing:2.4px}

  .face--window .pattern{inset:0}
  .window__title{position:absolute;left:0;right:0;top:6px;text-align:center;font-size:14px}
  .window__cut{position:absolute;left:36px;right:36px;top:28px;bottom:34px;background:var(--paper)}
</style>
</head>
<body>
<main class="canvas">
  <section class="stage">
    <div class="jar-label">
      <div class="jar-label__name">SILKEN MEADOW</div>
      <div class="jar-label__mark"></div>
      <div class="jar-label__scent">TURKISH ROSE</div>
    </div>
  </section>

  <section class="dieline">
    <div class="panel lid">
      <div class="pattern" role="img" aria-label="Faint light grey lattice pattern"></div>
      <div class="lid__plate">SILKEN MEADOW</div>
    </div>

    <div class="panel face face--front">
      <div class="lockup">
        <div class="lockup__dot"></div>
        <div class="lockup__name">SILKEN<br>MEADOW</div>
        <span class="scent-band">TURKISH ROSE</span>
      </div>
      <div class="contact">
        <div>+61 400 555 018 &nbsp;|&nbsp; hello@silkenmeadow-example.com.au</div>
        <div class="contact__web">www.silkenmeadow-example.com.au</div>
      </div>
    </div>

    <div class="panel face face--side-a">
      <div class="lockup">
        <div class="lockup__dot"></div>
        <div class="lockup__name">SILKEN<br>MEADOW</div>
        <span class="scent-band">TURKISH ROSE</span>
      </div>
    </div>

    <div class="panel face face--window">
      <div class="pattern" role="img" aria-label="Faint light grey lattice pattern framing the window"></div>
      <div class="window__title">SILKEN MEADOW</div>
      <div class="window__cut"></div>
    </div>

    <div class="panel face face--side-b">
      <div class="lockup">
        <div class="lockup__dot"></div>
        <div class="lockup__name">SILKEN<br>MEADOW</div>
        <span class="scent-band">TURKISH ROSE</span>
      </div>
    </div>
  </section>
</main>
</body>
</html>
```